I need 2 flyers designed for my business

Both can be similar in design and will have different purposes. I need an education based flyer and I need a government based flyer. The focus of the flyer will be software on the front and services on the back.
These all need to be 8.5x 11 in dimension (they can be full bleed). I would like to be able to print these out if needed. The design needs to look good with our website > www.brintalo.com

The software details are on the website.

```html
<!DOCTYPE html>
<html lang="en">
<head>
<meta charset="utf-8">
<title>Brintalo – Record Management Services &amp; Software</title>
<link rel="stylesheet" href="https://fonts.googleapis.com/css2?family=Poppins:ital,wght@0,400;0,500;0,600;0,700;0,800;1,600&display=swap">
<style>
  :root{
    --red:#8c1b22;
    --gold:#9a8433;
    --blue:#1c9fd9;
    --blue-soft:#5cc6ea;
    --blue-line:#a9d9f0;
    --navy:#0b3f78;
    --ink:#231f20;
    --text:#2b2b2b;
    --white:#ffffff;
    --mist:#ececec;
    --stage:#d9d9d9;
  }
  *{box-sizing:border-box;margin:0;padding:0}
  html,body{width:898px;height:1200px;overflow:hidden;background:var(--stage)}
  body{font-family:"Poppins",sans-serif;color:var(--text)}
  .canvas{position:relative;width:898px;height:1200px;overflow:hidden;background:var(--stage)}

  .page{position:absolute;top:312px;width:898px;height:1200px;overflow:hidden;background:var(--white);
        transform:scale(.48);transform-origin:0 0;box-shadow:0 4px 18px rgba(0,0,0,.25)}
  .page.front{left:12px}
  .page.back{left:455px}
  .shapes{position:absolute;inset:0}
  .abs{position:absolute}

  .brand{left:42px;top:40px;display:flex;align-items:center;gap:12px}
  .brand-mark{width:26px;height:26px;background:var(--gold)}
  .brand-name{font-weight:700;font-size:40px;letter-spacing:1px;color:var(--red);line-height:1}

  /* ---------- front ---------- */
  .site{right:38px;top:68px;font-size:21px;font-weight:500;color:var(--ink);letter-spacing:.5px}
  .headline{left:378px;top:160px;font-weight:800;font-size:60px;line-height:.98;color:var(--white);letter-spacing:.5px}
  .headline .accent{color:var(--gold)}
  .tagline{left:386px;top:432px;font-size:20px;line-height:1.2;color:var(--white)}
  .tagline em{font-weight:600}
  .section-label{left:40px;top:525px;font-weight:700;font-size:33px;color:var(--white);letter-spacing:.5px}
  .intro{left:40px;top:594px;width:430px;font-size:17.5px;line-height:1.22;color:var(--ink)}
  .features{top:708px;display:grid;gap:3px;font-size:17.5px;font-weight:500;color:var(--white)}
  .features li{list-style:none;display:flex;align-items:center;gap:14px}
  .features li::before{content:"›";color:var(--blue);font-weight:700;font-size:24px;line-height:1}
  .features.col-a{left:40px}
  .features.col-b{left:398px}
  .pill{height:38px;border-radius:19px;background:var(--gold);color:var(--white);font-weight:700;font-size:28px;line-height:38px;padding-left:34px}
  .pill.benefits{left:42px;top:830px;width:352px}
  .pill.provides{left:470px;top:830px;width:368px}
  .divider{left:434px;top:835px;width:1.5px;height:220px;background:#8a8a8a}
  .ticks li{list-style:none;position:relative;padding-left:28px;font-size:17.5px;line-height:1.22;color:var(--ink)}
  .ticks li::before{content:"";position:absolute;left:0;top:5px;width:13px;height:13px;border-radius:50%;background:var(--blue);box-shadow:inset 0 0 0 2px #bfe6f7}
  .ticks.benefits{left:56px;top:890px;width:370px}
  .ticks.benefits li{margin-bottom:18px}
  .ticks.provides{left:485px;top:890px;width:400px}
  .ticks.provides li{margin-bottom:5px}
  .contact{left:440px;top:1094px;font-size:20px;color:var(--white);white-space:nowrap}
  .contact b{font-weight:700}

  /* ---------- back ---------- */
  .service-title{left:151px;font-weight:700;font-size:28px;line-height:1.05;color:var(--blue);letter-spacing:.3px}
  .service-desc{left:39px;width:405px;font-size:17px;line-height:1.3;color:var(--ink)}
  .offer-box{left:466px;width:384px;border:2px solid var(--blue-line);border-radius:16px}
  .offer-label{left:505px;width:302px;background:var(--red);color:var(--white);border-radius:8px;padding:5px 20px;line-height:1.1}
  .offer-label b{display:block;font-weight:700;font-size:22px}
  .offer-label span{font-size:18px}
  .offer-label .lead{font-size:18px;font-weight:500}
  .offer-list{left:478px;width:354px;background:repeating-linear-gradient(var(--blue) 0 29px,var(--blue-soft) 29px 58px)}
  .offer-list li{list-style:none;position:relative;padding-left:34px;font-size:16.5px;font-weight:600;line-height:29px;color:var(--white)}
  .offer-list li::before{content:"✓";position:absolute;left:9px;top:7px;width:15px;height:15px;border-radius:50%;background:var(--white);color:var(--blue);font-size:11px;line-height:15px;text-align:center;font-weight:700}
  .rule{left:50px;width:800px;border-top:2px dashed #c9c9c9}
  .sales-title{left:405px;top:922px;font-weight:700;font-size:36px;color:var(--white);letter-spacing:.5px}
  .sales-line{left:414px;display:flex;align-items:center;gap:20px;font-size:27px;font-weight:600;color:var(--ink)}
  .sales-line small{font-size:20px;font-weight:400}
  .web{left:414px;top:1099px;font-size:21px;font-weight:500;letter-spacing:3px;color:var(--white)}
</style>
</head>
<body>
<div class="canvas">

  <!-- ================= FRONT: SOFTWARE ================= -->
  <main class="page front">
    <svg class="shapes" width="898" height="1200" viewBox="0 0 898 1200" aria-hidden="true">
      <defs>
        <linearGradient id="frontHero" x1="0" y1="0" x2="1" y2="1">
          <stop offset="0" stop-color="#1a6db3"/><stop offset=".55" stop-color="#0b4d8e"/><stop offset="1" stop-color="#1580c4"/>
        </linearGradient>
        <radialGradient id="frontGlow" cx=".5" cy=".5" r=".5">
          <stop offset=".8" stop-color="#1c9fd9" stop-opacity=".55"/><stop offset="1" stop-color="#1c9fd9" stop-opacity="0"/>
        </radialGradient>
      </defs>
      <path d="M300 150 C340 140 360 140 400 140 L898 140 L898 430 L330 430 Z" fill="url(#frontHero)"/>
      <path d="M898 418 L372 418 C300 418 300 520 220 520 L0 520 L0 575 L260 575 C350 575 380 492 460 492 L898 492 Z" fill="var(--red)"/>
      <path d="M0 575 L260 575 C350 575 380 492 460 492 L898 492 L898 500 L466 500 C390 500 360 585 260 585 L0 585 Z" fill="#e9e9e9"/>
      <rect x="0" y="678" width="898" height="122" fill="var(--ink)"/>
      <circle cx="200" cy="300" r="168" fill="url(#frontGlow)"/>
      <circle cx="200" cy="300" r="150" fill="var(--white)"/>
      <circle cx="200" cy="300" r="144" fill="none" stroke="var(--blue)" stroke-width="8"/>
      <rect x="0" y="1148" width="898" height="52" fill="var(--mist)"/>
      <rect x="190" y="1086" width="720" height="52" rx="26" fill="var(--blue)"/>
      <rect x="360" y="1086" width="560" height="52" rx="26" fill="var(--red)"/>
    </svg>

    <div class="abs" role="img" aria-label="Person touching a glowing digital document icon surrounded by file icons"
         style="left:66px;top:166px;width:268px;height:268px;border-radius:50%;background:radial-gradient(circle at 55% 45%,#8fb7d9 0%,#2f5f8f 40%,#15304f 100%)"></div>
    <div class="abs" role="img" aria-label="Businessman in a suit holding a tablet with a checkmark icon"
         style="left:574px;top:542px;width:292px;height:162px;border:6px solid var(--white);box-shadow:0 2px 8px rgba(0,0,0,.25);background:linear-gradient(120deg,#6d747c 0%,#3b4148 45%,#1f2a36 100%)"></div>

    <div class="abs brand"><span class="brand-mark"></span><span class="brand-name">BRINTALO</span></div>
    <div class="abs site">www.brintalo.com</div>

    <h1 class="abs headline">RECORD<br>MANAGEMENT<br>SERVICES &amp;<br><span class="accent">SOFTWARE</span></h1>
    <p class="abs tagline">Spend time <em>using</em> your information<br>instead of <em>searching</em> for it.</p>

    <h2 class="abs section-label">SOFTWARE</h2>
    <p class="abs intro">Access all of your records – whether active or inactive – through VaultView, our comprehensive records management software.</p>

    <ul class="abs features col-a">
      <li>Document Archive</li><li>Electronic Forms &amp; Worflows</li><li>HR Onboarding</li>
    </ul>
    <ul class="abs features col-b">
      <li>eSigning</li><li>Mileage &amp; Expense Tracking</li><li>Scanning &amp; Database Conversion</li>
    </ul>

    <h3 class="abs pill benefits">BENEFITS</h3>
    <div class="abs divider"></div>
    <h3 class="abs pill provides">VAULTVIEW PROVIDES</h3>

    <ul class="abs ticks benefits">
      <li>Enjoy both web-based access to your records or access them on the go using our mobile app.</li>
      <li>Includes 3rd party integration tools.</li>
      <li>Protects records with disaster recovery and redundancy features.</li>
    </ul>
    <ul class="abs ticks provides">
      <li>Electronic forms</li><li>Workflow automation</li><li>Automated system/email notifications</li>
      <li>Full text search capabilities</li><li>Audit tracking (including HIPAA)</li><li>Redaction &amp; annotation capabilities</li>
    </ul>

    <p class="abs contact">Call: <b>(555) 214-3060</b> | Fax: <b>(555) 214-3061</b></p>
  </main>

  <!-- ================= BACK: SERVICES ================= -->
  <section class="page back">
    <svg class="shapes" width="898" height="1200" viewBox="0 0 898 1200" aria-hidden="true">
      <defs>
        <radialGradient id="backGlow" cx=".5" cy=".5" r=".5">
          <stop offset=".8" stop-color="#1c9fd9" stop-opacity=".5"/><stop offset="1" stop-color="#1c9fd9" stop-opacity="0"/>
        </radialGradient>
      </defs>
      <!-- hero banner frame -->
      <rect x="290" y="20" width="660" height="116" rx="58" fill="var(--white)" stroke="#e3e3e3" stroke-width="2"/>

      <!-- icon tabs -->
      <g fill="var(--gold)">
        <path d="M0 160 H105 a41 41 0 0 1 0 82 H0 Z"/>
        <path d="M0 410 H105 a41 41 0 0 1 0 82 H0 Z"/>
        <path d="M0 660 H105 a41 41 0 0 1 0 82 H0 Z"/>
      </g>
      <g fill="none" stroke="var(--white)" stroke-width="3" stroke-linejoin="round" stroke-linecap="round">
        <!-- stacked sheets -->
        <path d="M40 186 L75 172 L110 186 L75 200 Z"/>
        <path d="M40 198 L75 212 L110 198"/>
        <path d="M40 210 L75 224 L110 210"/>
        <!-- padlock -->
        <rect x="55" y="446" width="40" height="32" rx="3"/>
        <path d="M62 446 V434 a13 13 0 0 1 26 0 V446"/>
        <!-- archive box -->
        <rect x="50" y="680" width="50" height="12" rx="2"/>
        <rect x="54" y="692" width="42" height="34"/>
        <path d="M66 703 H84 M66 711 H84"/>
      </g>

      <!-- sales band -->
      <path d="M250 972 C300 972 320 910 390 910 L898 910 L898 972 Z" fill="var(--gold)"/>
      <rect x="0" y="1000" width="160" height="50" fill="var(--gold)"/>
      <circle cx="192" cy="1054" r="136" fill="url(#backGlow)"/>
      <circle cx="192" cy="1054" r="118" fill="var(--white)"/>
      <circle cx="192" cy="1054" r="112" fill="none" stroke="var(--blue)" stroke-width="7"/>

      <!-- phone + mail icons -->
      <path d="M418 996 c-3 3 -3 8 2 14 l6 7 c5 5 10 6 13 3 l3 -3 -7 -7 -3 3 c-2 -1 -7 -6 -8 -8 l3 -3 -7 -7 Z" fill="var(--gold)"/>
      <rect x="414" y="1036" width="30" height="20" fill="var(--gold)"/>
      <path d="M414 1036 L429 1048 L444 1036" fill="none" stroke="var(--white)" stroke-width="2"/>

      <!-- footer -->
      <rect x="330" y="1080" width="620" height="60" rx="30" fill="var(--blue)"/>
      <rect x="352" y="1090" width="600" height="56" rx="28" fill="var(--red)"/>
    </svg>

    <div class="abs" role="img" aria-label="Dark blue digital network banner with glowing cloud upload icons"
         style="left:300px;top:30px;width:598px;height:96px;border-radius:48px 0 0 48px;background:linear-gradient(100deg,#0e2a55 0%,#12508e 50%,#0b2d5c 100%)"></div>

    <div class="abs brand"><span class="brand-mark"></span><span class="brand-name">BRINTALO</span></div>

    <!-- scanning -->
    <h2 class="abs service-title" style="top:160px">DOCUMENT<br>SCANNING SERVICES</h2>
    <p class="abs service-desc" style="top:258px">Fast, efficient process for the conversion of existing paper records to digital archives, increasing access and reducing onsite storage and costs.</p>
    <div class="abs offer-box" style="top:198px;height:166px"></div>
    <div class="abs offer-label" style="top:170px"><b>Scanning Services</b><span>for any format:</span></div>
    <ul class="abs offer-list" style="top:232px">
      <li>Standard Office Documents</li><li>16mm, 35mm Roll Microfilm</li>
      <li>Microfiche (Jackets or COM)</li><li>Large Format Documents/Drawings</li>
    </ul>

    <div class="abs rule" style="top:387px"></div>

    <!-- storage -->
    <h2 class="abs service-title" style="top:410px">DOCUMENT<br>STORAGE SERVICES</h2>
    <p class="abs service-desc" style="top:508px">Solution for offsite document storage and retrieval to effectively store, manage, and safeguard your vital business records and documents.</p>
    <div class="abs offer-box" style="top:448px;height:166px"></div>
    <div class="abs offer-label" style="top:420px"><span class="lead">A local, </span><b style="display:inline">Convenient</b><br><b>Solution</b></div>
    <ul class="abs offer-list" style="top:482px">
      <li>Free Up Office Space</li><li>Reduce Costs</li>
      <li>Keep Records in a Fireproof,</li><li>Waterproof &amp; Wind-Safe Facility</li>
    </ul>

    <div class="abs rule" style="top:639px"></div>

    <!-- shredding -->
    <h2 class="abs service-title" style="top:660px">SECURE DOCUMENT<br>SHREDDING</h2>
    <p class="abs service-desc" style="top:758px">Safely and cost-effectively destroy unnecessary paper-based documents. One-time or recurring, our solutions are tailored to you.</p>
    <div class="abs offer-box" style="top:698px;height:196px"></div>
    <div class="abs offer-label" style="top:670px"><span class="lead">Destroy </span><b style="display:inline">Unnecessary</b><br><b>Documents</b></div>
    <ul class="abs offer-list" style="top:732px">
      <li>Protect confidential information</li>
      <li>Reduce the cost of managing information that is no longer useful</li>
      <li>Ensure compliance with regulations for information destruction</li>
    </ul>

    <!-- sales -->
    <div class="abs" role="img" aria-label="Office worker carrying a tall stack of binders"
         style="left:86px;top:948px;width:212px;height:212px;border-radius:50%;background:radial-gradient(circle at 50% 40%,#e7ecf1 0%,#9fb0c2 50%,#3c4f66 100%)"></div>
    <h2 class="abs sales-title">SALES INQUIRIES TO</h2>
    <p class="abs sales-line" style="top:986px;left:462px">(555) 214-3060 <small>or</small></p>
    <p class="abs sales-line" style="top:1026px;left:462px">support@brintalo.com</p>
    <p class="abs web">www.brintalo.com</p>
  </section>

</div>
</body>
</html>
```